Looking for a "Hipster orientated" menu design for our espresso bar.
Lantern Brewhouse is part of the Marlow Kettle Group a leading Australian roasting company.
We are leaving the brief open as we don't to use any pre-conceived ideas that are in our heads. In a nutshell we don't want to be an imitation of others.
Lantern Brewhouse is an industrial inspired space with some classic elements. Coffee is our passion and simple fresh well presented food to match using the best local ingredients.

We would like our menu to have a clear distinction between beverages and food.
An open A4 size menu landscape format is ideal or perhaps folded.

This is our first crowd sourced design and the menu is a test to what will be a new webpage, online store and new brand elements for our company to the right designer.

At this stage don't worry about content i.e whats in a sandwich. Random latin under the word breakfast burger is fine.

Good luck

Target Market(s)

Hipster caffeine and food addicts

Industry/Entity Type

Industrial

Font styles to use
Decorative

Colors

Designer to choose colors to be used in the design.

Requirements
Must have
• A distinction between breakfast, lunch and beverages/coffee
Should not have
• overcrowded, hard to read

```html
<!DOCTYPE html>
<html lang="en">
<head>
<meta charset="utf-8">
<title>Lantern Brewhouse — Menu</title>
<link rel="stylesheet" href="https://fonts.googleapis.com/css2?family=Lobster&family=Raleway:wght@400;700&family=Arvo:wght@700&display=swap">
<style>
  :root {
    --menu-orange: #ee7b2f;
    --menu-orange-light: #f4935a;
    --ink-white: #ffffff;
    --title-grey: #dfe1e4;
    --frame-line: #fbe3d2;
  }
  * { margin: 0; padding: 0; box-sizing: border-box; }
  html, body { width: 1200px; height: 849px; overflow: hidden; background: var(--menu-orange); }
  .menu {
    position: relative; width: 1200px; height: 849px; overflow: hidden;
    background: var(--menu-orange); color: var(--ink-white);
    font-family: "Raleway", Arial, sans-serif; text-align: center;
  }
  .backdrop-art { position: absolute; inset: 0; }
  .frames { position: absolute; inset: 0; }

  .title-spine {
    position: absolute; left: 83px; top: 397px; width: 810px; height: 56px;
    transform: rotate(-90deg); transform-origin: 50% 50%;
    font-family: "Arvo", Georgia, serif; font-weight: 700; color: var(--title-grey);
    font-size: 46px; line-height: 56px; letter-spacing: 6px; white-space: nowrap;
    text-align: center; text-transform: uppercase; overflow: hidden;
  }
  .title-spine .initial { font-size: 56px; }

  .drinks-column { position: absolute; left: 57px; width: 400px; }
  .drinks-section { position: absolute; left: 0; width: 400px; }
  .drinks-section h2 {
    font-family: "Lobster", cursive; font-weight: 400; font-size: 24px; line-height: 30px;
  }
  .drinks-section p { font-size: 17px; line-height: 20.5px; }
  .drinks-section .price { font-weight: 700; font-size: 13px; letter-spacing: 1px; }

  .food-block { position: absolute; }
  .food-block h2 {
    font-family: "Lobster", cursive; font-weight: 400; font-size: 23px; line-height: 28px;
    margin-bottom: 7px;
  }
  .food-block h3 {
    font-family: "Lobster", cursive; font-weight: 400; font-size: 16px; line-height: 22px;
    margin-bottom: 9px;
  }
  .food-item { margin-bottom: 9.3px; }
  .food-item .desc { font-size: 12.5px; line-height: 16px; }
  .food-item .price { font-weight: 700; font-size: 10px; line-height: 14px; letter-spacing: 0.8px; }
</style>
</head>
<body>
<main class="menu">
  <svg class="backdrop-art" width="1200" height="849" role="img" aria-label="Faint vintage car front illustration in soft orange tones">
    <path d="M160 690 C150 560 170 470 260 430 C300 250 360 120 600 110 C840 120 900 250 940 430 C1030 470 1050 560 1040 690 Z" fill="var(--menu-orange-light)" opacity="0.35"/>
  </svg>

  <svg class="frames" width="1200" height="849" aria-hidden="true">
    <g fill="none" stroke="var(--frame-line)" stroke-width="1.5">
      <path d="M18 12 H452 A8 8 0 0 0 460 20 V829 A8 8 0 0 0 452 837 H18 A8 8 0 0 0 10 829 V20 A8 8 0 0 0 18 12 Z"/>
      <path d="M22 16 H448 A8 8 0 0 0 456 24 V825 A8 8 0 0 0 448 833 H22 A8 8 0 0 0 14 825 V24 A8 8 0 0 0 22 16 Z"/>
      <path d="M530 12 H1182 A8 8 0 0 0 1190 20 V829 A8 8 0 0 0 1182 837 H530 A8 8 0 0 0 522 829 V20 A8 8 0 0 0 530 12 Z"/>
      <path d="M534 16 H1178 A8 8 0 0 0 1186 24 V825 A8 8 0 0 0 1178 833 H534 A8 8 0 0 0 526 825 V24 A8 8 0 0 0 534 16 Z"/>
      <line x1="464" y1="14" x2="464" y2="835"/>
      <line x1="516" y1="14" x2="516" y2="835"/>
    </g>
  </svg>

  <h1 class="title-spine"><span class="initial">L</span>antern <span class="initial">B</span>rewhouse</h1>

  <section class="drinks-column" aria-label="Beverages">
    <div class="drinks-section" style="top:42px">
      <h2>Coffee</h2>
      <p>Rior assin escilique se veribus tisquiae.</p><p class="price">$3.50</p>
      <p>Rior assin escilique se veribus tisquiae.</p><p class="price">$3.50</p>
    </div>
    <div class="drinks-section" style="top:200px">
      <h2>Traditional Espresso</h2>
      <p>Rior assin escilique se veribus tisquiae.</p><p class="price">$3.50</p>
      <p>Rior assin escilique se veribus tisquiae.</p><p class="price">$3.50</p>
    </div>
    <div class="drinks-section" style="top:358px">
      <h2>Blended Drinks</h2>
      <p>Ehent, qui quam re latur tisquiae.</p><p class="price">$3.50</p>
      <p>Rior assin escilique se veribus tisquiae.</p><p class="price">$3.50</p>
    </div>
    <div class="drinks-section" style="top:516px">
      <h2>Tea</h2>
      <p>Nem elendi ipitate plabo.</p><p class="price">$3.50</p>
      <p>Rior assin escilique se veribus tisquiae.</p><p class="price">$3.50</p>
    </div>
    <div class="drinks-section" style="top:674px">
      <h2>Other Drinks</h2>
      <p>Videm rem ilibeatem<br>ipsam que quibus dolorpo.</p><p class="price">$3.50</p>
      <p>Rior assin escilique se veribus tisquiae.</p><p class="price">$3.50</p>
    </div>
  </section>

  <section aria-label="Food">
    <div class="food-block" style="left:698px; width:300px; top:31px">
      <h2>Breakfast</h2>
      <div class="food-item"><p class="desc">Rior assin escilique se veribus tisquiae.</p><p class="price">$5.50</p></div>
      <div class="food-item"><p class="desc">Rior assin escilique se veribus tisquiae.</p><p class="price">$5.50</p></div>
      <div class="food-item"><p class="desc">Rior assin escilique se veribus tisquiae.</p><p class="price">$5.50</p></div>
      <div class="food-item"><p class="desc">Rior assin escilique se veribus tisquiae.</p><p class="price">$5.50</p></div>
      <div class="food-item"><p class="desc">Rior assin escilique se veribus tisquiae.</p><p class="price">$5.50</p></div>
    </div>
    <div class="food-block" style="left:698px; width:300px; top:291px">
      <h2>Lunch</h2>
      <div class="food-item"><p class="desc">Rior assin escilique se veribus tisquiae.</p><p class="price">$8.50</p></div>
      <div class="food-item"><p class="desc">Rior assin escilique se veribus tisquiae.</p><p class="price">$8.50</p></div>
      <div class="food-item"><p class="desc">Rior assin escilique se veribus tisquiae.</p><p class="price">$8.50</p></div>
      <div class="food-item"><p class="desc">Rior assin escilique se veribus tisquiae.</p><p class="price">$8.50</p></div>
      <div class="food-item"><p class="desc">Rior assin escilique se veribus tisquiae.</p><p class="price">$8.50</p></div>
    </div>
    <div class="food-block" style="left:568px; width:280px; top:530px">
      <h3>Soup</h3>
      <div class="food-item"><p class="desc">Rior assin escilique se veribus tisquiae.</p><p class="price">$4.50</p></div>
      <div class="food-item"><p class="desc">Rior assin escilique se veribus tisquiae.</p><p class="price">$4.50</p></div>
    </div>
    <div class="food-block" style="left:848px; width:280px; top:530px">
      <h3>Salad</h3>
      <div class="food-item"><p class="desc">Rior assin escilique se veribus tisquiae.</p><p class="price">$4.50</p></div>
      <div class="food-item"><p class="desc">Rior assin escilique se veribus tisquiae.</p><p class="price">$4.50</p></div>
    </div>
    <div class="food-block" style="left:698px; width:300px; top:667px">
      <h2>Desserts</h2>
      <div class="food-item"><p class="desc">Rior assin escilique se veribus tisquiae.</p><p class="price">$4.00</p></div>
      <div class="food-item"><p class="desc">Rior assin escilique se veribus tisquiae.</p><p class="price">$4.00</p></div>
      <div class="food-item"><p class="desc">Rior assin escilique se veribus tisquiae.</p><p class="price">$4.00</p></div>
    </div>
  </section>
</main>
</body>
</html>
```